Marketing Services Flyer

We need a flyer for a new company based in Annapolis, MD called Bramblecove Outreach. We offer Social Media Management, Traditional Media Ad Design/Placement, Professional Video Production, Email Marketing and Graphic Design services. This flyer will serve as a leave behind/sales flyer to promote our services. I have attached the logo. The font in the logo is Helvetica Neue Light STD.

Tag line:

Bramblecove Outreach
Strategic Marketing and Integrated Communications
Updates

I need another section added under the services I offer.  Please add this in along with the others. 

Custom Content

• Blogging - We will develop a strategy, write your blog and promote it via social media
• Press Releases - We will write press releases about exciting developments in your business and get them posted in places where reporters will actually see them. 
• Reviews - We will gather and post reviews of your business from your customers 

Target Market(s)

This is targeted to business owners who are too busy to do their own online marketing.

Industry/Entity Type

Graphic Design

Requirements
Must have
• I would like this flyer to have a front and back page so that I may print a double sided flyer. I have a logo that will need to be included. I want to illustrate the services I can provide with pictures and text. For example, for Social Media Management I would like the logo for Chirpline, Facepage, Gather +, Places, WorkNet, etc.

I have attached pictures of local lifestyle magazines that I would like used to illustrate my Traditional Media Ad services. Please use these images or other images of the same publications if you find better ones.

I will provide copy in an attachment.

Must include contact information and Social Media addresses.

Chirpline.com/BramblecoveOut
Facepage.com/BCOut
Vidstream.com/BramblecoveOut

phone - 410.555.0148
email - info@bramblecoveoutreach.example
Nice to have
• A screwpile lighthouse is a type of lighthouse found on Chesapeake Bay. If it works it would be nice to incorporate images of these somehow, if it does not work that is fine.

Include this copy in an eye catching way:

Social - Email - INTEGRATED - Video - Design

I have a background vector image file I will attach to this. I bought it so if you think it would add to the design then use it, or use part of it. If you don't think it adds to the design then leave it off, up to you.

```html
<!DOCTYPE html>
<html lang="en">
<head>
<meta charset="utf-8">
<title>Bramblecove Outreach – Strategic Marketing &amp; Integrated Communications</title>
<link href="https://fonts.googleapis.com/css2?family=Roboto+Condensed:wght@300;400;700&family=Roboto:wght@300;400;700&display=swap" rel="stylesheet">
<style>
  :root {
    --blue-light: #0a78c2;
    --blue-mid: #0868ad;
    --blue-dark: #075a98;
    --ampersand: #0c4f86;
    --yellow: #fccc0a;
    --ink: #111111;
    --white: #ffffff;
    --grey: #7d8085;
    --grey-text: #4a4a4a;
  }
  * { box-sizing: border-box; margin: 0; padding: 0; }
  html, body { width: 927px; height: 1200px; overflow: hidden; background: var(--white); }
  .flyer {
    position: relative;
    width: 927px;
    height: 1200px;
    overflow: hidden;
    background: var(--white);
    font-family: "Roboto Condensed", "Helvetica Neue", Arial, sans-serif;
  }
  .hero {
    position: absolute;
    left: 0; top: 0;
    width: 927px; height: 856px;
    background: linear-gradient(160deg, var(--blue-dark) 0%, var(--blue-light) 45%, var(--blue-mid) 100%);
  }
  .service-band {
    position: absolute;
    left: 0; top: 111px;
    width: 927px; height: 56px;
    background: var(--yellow);
    color: var(--ink);
    font-family: "Roboto", Arial, sans-serif;
    font-size: 30px;
    font-weight: 400;
    line-height: 56px;
    text-align: center;
  }
  .ampersand {
    position: absolute;
    left: 340px; top: 298px;
    font-family: "Roboto", Arial, sans-serif;
    font-weight: 700;
    font-size: 300px;
    line-height: 1;
    color: var(--ampersand);
  }
  .headline {
    position: absolute;
    left: 0; width: 927px;
    display: block;
    text-align: center;
    color: var(--white);
    text-shadow: 2px 3px 3px rgba(0,0,0,0.45);
    line-height: 1;
  }
  .headline-top { top: 280px; font-size: 72px; letter-spacing: -1px; }
  .headline-top .strong { font-weight: 700; }
  .headline-top .light { font-weight: 400; }
  .headline-main {
    top: 492px;
    font-size: 154px;
    font-weight: 700;
    letter-spacing: -3px;
    background: linear-gradient(180deg, #ffffff 55%, #d5d8dd 100%);
    -webkit-background-clip: text;
    background-clip: text;
    color: transparent;
    filter: drop-shadow(2px 4px 3px rgba(0,0,0,0.45));
    text-shadow: none;
  }
  .headline-sub {
    top: 636px;
    font-size: 86px;
    font-weight: 400;
    letter-spacing: -2px;
    transform: scaleX(0.94);
  }
  .pointer {
    position: absolute;
    left: 436px; top: 855px;
    width: 58px; height: 40px;
  }
  .brand {
    position: absolute;
    left: 0; top: 985px;
    width: 927px;
    text-align: center;
  }
  .brand-name {
    display: inline-flex;
    align-items: center;
    gap: 12px;
    font-size: 42px;
    font-weight: 300;
    color: var(--grey);
  }
  .brand-mark {
    width: 18px; height: 18px;
    background: var(--grey);
  }
  .contact {
    position: absolute;
    left: 0; top: 1117px;
    width: 927px;
    text-align: center;
    font-family: "Roboto", Arial, sans-serif;
    font-size: 19px;
    color: var(--grey-text);
  }
  .contact .divider { margin: 0 10px; }
</style>
</head>
<body>
<main class="flyer">
  <section class="hero">
    <div class="service-band">Social - Email - Content - Video - Design</div>
    <div class="ampersand" aria-hidden="true">&amp;</div>
    <h1>
      <span class="headline headline-top"><span class="strong">Strategic</span><span class="light">MARKETING</span></span>
      <span class="headline headline-main">Integrated</span>
      <span class="headline headline-sub">COMMUNICATIONS</span>
    </h1>
  </section>
  <svg class="pointer" viewBox="0 0 58 40" aria-hidden="true">
    <polygon points="0,0 58,0 29,40" fill="#0868ad"/>
  </svg>
  <div class="brand">
    <div class="brand-name"><span class="brand-mark"></span>Bramblecove Outreach</div>
  </div>
  <p class="contact">Ph: 410.555.0148<span class="divider">||</span>info@bramblecoveoutreach.example</p>
</main>
</body>
</html>
```